Flyer-Design für nachhaltige Spülbecher aus Keramik
Zielgruppe
Zielgruppe des Flyers sind Zahnärzte. Wir fertigen die ersten nachhaltigen Spülbecher für Praxen aus Keramik.
Aufgabenstellung
Der Flyer soll einen hochwertigen und exklusiven Eindruck hinterlassen.
Auf dem Flyer sollte das Logo, Kontaktmöglichkeiten, Anschrift, 1-2 Bilder des Produktes und ein kleiner Text bezüglich Nachhaltigkeit vorhanden sein. Die aktuell hochgeladenen Bilder der Becher sind aktuell noch Platzhalter, es werden in den nächsten Tagen die richtigen Bilder hochgeladen.
WICHTIG: Bitte einen Platzhalter für eine Überschrift und Stichpunkte/Informationen einarbeiten. Leider ist noch nicht Final klar wir diese Lauten soll, daher wird dieser Teil noch von mir noch selbst ergänzt. Danke
Website: www.lindgau-keramik.de

```html
<!DOCTYPE html>
<html lang="de">
<head>
<meta charset="utf-8">
<title>Lindgau Keramik – Flyer</title>
<link rel="stylesheet" href="https://fonts.googleapis.com/css2?family=Montserrat:wght@400;500&family=Open+Sans:wght@400&family=Roboto+Slab:wght@400;700&display=swap">
<style>
  :root {
    --stage: #e9e9e9;
    --ink-dark: #262626;
    --paper: #ffffff;
    --text-light: #f2f2f2;
    --text-body: #d6d6d6;
    --text-grey: #8a8a8a;
    --text-black: #1d1d1d;
  }
  * { box-sizing: border-box; margin: 0; padding: 0; }
  html, body { width: 1200px; height: 625px; overflow: hidden; }
  body {
    background: var(--stage);
    display: flex;
    align-items: center;
    justify-content: center;
    gap: 60px;
  }
  .page {
    position: relative;
    width: 390px;
    height: 552px;
    box-shadow: 0 6px 18px rgba(0,0,0,.18);
    overflow: hidden;
  }

  /* Inside page */
  .inside { background: var(--ink-dark); }
  .inside .cups-photo {
    position: absolute; left: 0; top: 0; width: 250px; height: 280px;
    background: radial-gradient(ellipse at 55% 50%, #8fa7b3 0%, #6f7c80 30%, #2b2b2b 75%, #151515 100%);
  }
  .inside .headline {
    position: absolute; left: 0; top: 0; width: 36px; height: 280px;
    display: flex; align-items: center; justify-content: center;
  }
  .inside .headline span {
    display: block;
    transform: rotate(-90deg);
    white-space: nowrap;
    font-family: "Roboto Slab", serif;
    font-weight: 400;
    font-size: 27px;
    letter-spacing: 1px;
    color: transparent;
    -webkit-text-stroke: 0.8px rgba(255,255,255,.75);
  }
  .inside .brand-column {
    position: absolute; left: 250px; top: 0; width: 140px; height: 280px;
    background: var(--paper);
    display: flex; flex-direction: column; align-items: center;
    padding-top: 32px;
  }
  .brand-small { display: flex; align-items: center; gap: 5px; }
  .brand-small .mark { width: 9px; height: 9px; border: 1px solid var(--text-black); }
  .brand-small .name {
    font-family: "Montserrat", sans-serif; font-weight: 500; font-size: 9px; color: var(--text-black);
  }
  .brand-column .tagline {
    margin-top: 3px;
    font-family: "Montserrat", sans-serif; font-size: 5px; color: var(--text-black);
  }
  .inside .cup-photo {
    position: absolute; left: 250px; top: 280px; width: 140px; height: 272px;
    background: linear-gradient(180deg, #e4e4e2 0%, #cfd1d0 45%, #3f7d9c 62%, #2f6f90 72%, #e6e6e4 85%, #f2f2f0 100%);
  }
  .inside .body-text {
    position: absolute; left: 54px; top: 366px; width: 138px;
    font-family: "Open Sans", sans-serif; font-size: 7.4px; line-height: 1.3;
    color: var(--text-body);
  }

  /* Cover page */
  .cover { background: var(--paper); }
  .cover .cover-top {
    position: absolute; left: 0; top: 0; width: 100%; height: 284px;
    background: var(--ink-dark);
    display: flex; flex-direction: column; align-items: center; justify-content: center;
    padding-top: 20px;
  }
  .cover .brand-mark { width: 34px; height: 34px; border: 1.5px solid var(--text-light); margin-bottom: 16px; }
  .cover .brand-name {
    font-family: "Montserrat", sans-serif; font-weight: 500; font-size: 15px; color: var(--text-light);
  }
  .cover .address {
    position: absolute; right: 32px; top: 304px; text-align: right;
    font-style: normal;
    font-family: "Montserrat", sans-serif; font-size: 10.5px; line-height: 1.35; color: var(--text-grey);
  }
  .cover .address .company {
    font-family: "Roboto Slab", serif; font-weight: 700; font-size: 12px; color: var(--text-black);
    margin-bottom: 4px;
  }
  .cover .contact {
    position: absolute; left: 32px; bottom: 38px;
    font-family: "Roboto Slab", serif; font-weight: 700; font-size: 12px; line-height: 1.2; color: var(--text-black);
  }
</style>
</head>
<body>

  <section class="page inside">
    <div class="cups-photo" role="img" aria-label="Produktfoto: farbige Keramik-Spülbecher in Rosé, Hellblau, Grün, Grau und Weiß auf dunklem Grund"></div>
    <h2 class="headline"><span>NAME BECHER</span></h2>
    <div class="brand-column">
      <div class="brand-small"><span class="mark"></span><span class="name">Lindgau Keramik</span></div>
      <p class="tagline">Handgefertigt für Ihre Praxis.</p>
    </div>
    <div class="cup-photo" role="img" aria-label="Produktfoto: blauer Keramik-Spülbecher unter dem Wasserhahn einer Behandlungseinheit"></div>
    <p class="body-text">Itatios ipit at. Osaniente magnatur? Ruptate ssimaio moluptatur? Solut quos apis autest, net fugiatatem volo ipsam que corum fugiatur? Qui nonsequ iasinverest, optatur emporempos num iliqui dest, nulla­borunt, inisciis aligni sequo dolum-</p>
  </section>

  <section class="page cover">
    <div class="cover-top">
      <span class="brand-mark"></span>
      <h1 class="brand-name">Lindgau Keramik GmbH</h1>
    </div>
    <address class="address">
      <p class="company">Lindgau Keramik GmbH</p>
      <p>Brunnenweg 8</p>
      <p>98631 Lindgau</p>
    </address>
    <p class="contact">info@lindgau-keramik.de<br>0176 / 28461937</p>
  </section>

</body>
</html>
```